Music teacher for flute, beinning piano and a Songs and Steps class

I would like a FB page where folks could contact me for flute and beginning piano lessons OR for a Songs and Steps class (low-impact exercises, singing, work with drumming/rhythms to alleviate the symptoms of Parkinson's disease.) I have a FB page for the Songs and Steps but not for music lessons.
https://www.friendlane.net/SongsandStepsRoseville
I would want a different url since I am no longer doing this in Roseville, CA but Sacramento, CA

Hello, forgive me for dropping out of contact. Can you tell me if there was a fake FB page created under the username Songs and Steps Sacramento? It's surprisingly close to what I offer but it says "Painting class" and other misinformation. Any information would be helpful, thanks. I'd like to switch my username to Songs and Steps Sacramento, if possible.

```html
<!DOCTYPE html>
<html lang="en">
<head>
<meta charset="utf-8">
<title>Songs and Steps – Freedom of Expression</title>
<link rel="stylesheet" href="https://fonts.googleapis.com/css2?family=Poppins:wght@600;700&family=Roboto+Condensed:wght@700&display=swap">
<style>
  :root {
    --mustard: #f1b234;
    --mustard-deep: #e39a28;
    --navy: #1f2b3a;
    --coral: #f04848;
    --white: #ffffff;
    --amber: #f4a62a;
    --brown: #5a2a10;
    --photo-warm: #c47a2e;
    --photo-dark: #6e3d18;
  }
  * { margin: 0; padding: 0; box-sizing: border-box; }
  html, body { width: 1200px; height: 527px; overflow: hidden; background: var(--mustard); }
  .banner {
    position: relative;
    width: 1200px;
    height: 527px;
    overflow: hidden;
    background: linear-gradient(100deg, var(--mustard) 0%, var(--mustard) 55%, var(--mustard-deep) 100%);
    font-family: "Poppins", sans-serif;
  }
  .brush-shapes { position: absolute; inset: 0; width: 1200px; height: 527px; }
  .performer-photo {
    position: absolute;
    left: 690px; top: 0;
    width: 510px; height: 527px;
    background: linear-gradient(90deg, rgba(196,122,46,0) 0%, rgba(196,122,46,0.75) 22%, var(--photo-warm) 45%, var(--photo-dark) 100%);
  }
  .title {
    position: absolute;
    left: 172px; top: 62px;
    color: var(--white);
    font-weight: 700;
    font-size: 70px;
    line-height: 74px;
    letter-spacing: 0;
  }
  .title__join {
    color: var(--amber);
    font-size: 36px;
    font-weight: 700;
    margin-left: 6px;
  }
  .tagline {
    position: absolute;
    left: 171px; top: 300px;
    color: var(--white);
    font-weight: 600;
    font-size: 33px;
    line-height: 40px;
  }
  .mission {
    position: absolute;
    left: 172px; top: 338px;
    color: var(--white);
    font-family: "Roboto Condensed", sans-serif;
    font-weight: 700;
    font-size: 27px;
    line-height: 34px;
  }
  .audience {
    position: absolute;
    left: 176px; top: 464px;
    color: var(--brown);
    font-weight: 600;
    font-size: 19px;
    line-height: 26px;
  }
</style>
</head>
<body>
<main class="banner">
  <svg class="brush-shapes" viewBox="0 0 1200 527" aria-hidden="true">
    <path fill="#1f2b3a" d="M0 0 H860 C850 40 860 70 836 100 C810 130 790 160 760 178 C720 200 660 206 610 222 C540 244 460 240 390 250 C320 260 250 252 190 262 C120 272 60 236 0 222 Z"/>
    <path fill="#f04848" d="M136 284 C220 266 330 270 420 266 C520 262 610 258 684 270 C676 300 692 336 672 376 C600 388 520 380 430 388 C330 396 240 384 170 392 C150 378 130 352 138 330 C122 314 132 298 136 284 Z"/>
  </svg>

  <div class="performer-photo" role="img" aria-label="Warm-toned photo of a young woman playing the flute with a pianist at an upright piano behind her, with scattered music notes"></div>

  <h1 class="title">SONGS<span class="title__join">and</span><br>STEPS</h1>
  <p class="tagline">freedom of expression</p>
  <p class="mission">Using music to improve the lives of folks</p>
  <p class="audience">with Parkinson’s Disease</p>
</main>
</body>
</html>
```